Recto Verso Audiology Business Card

Business card with a beautiful design on the back. On the Recto you need the following data Vandrell Osko Audiologist Hearing Solutions Hearing Protection Tinnitus Hyperacusis Tel: 0482/37 58 90 Email: On the back, you need something nice like the attached file. The logo "Corra Nube" can be in the center The colors of the Logo can not be changed If possible stay in the same colors as the logo Another solution is to put the logo on the front and have a nice back (A mosaic of small ears, hearing aids or other ..) Thank you _______________________________________________________________ Visit card On the Recto Vandrell Osko Audiologist Hearing Solutions Hearing Protection Tinnitus Hyperacusis Tel: 0482/37 58 90 Email: You can put the logo " Corra Nube "on the Recto of the Verso The colors of the logo can not be changed. If you put the logo on the back, it must be well integrated. On the Verso I need something in the files. something stylish. It's a visit card for an audiologist. You can get ears of hearing aids if you need. Thanks

Target Market(s)

customers

Contact Information for Business Card

Carte de visite standard ou A6

Font styles to use
Serif
Sans Serif

Colors
33a6d7

Requirements
Must have
• the logo and a stylized background.
Nice to have
• It would be nice to have a back side related to audiology (ears, hearing aids etc.)

```html
<!DOCTYPE html>
<html lang="fr">
<head>
<meta charset="utf-8">
<title>Vandrell Osko – Audiologue</title>
<link rel="stylesheet" href="https://fonts.googleapis.com/css2?family=Open+Sans:wght@400;600;700&display=swap">
<style>
  :root {
    --card-teal: #00aebf;
    --ink-light: #f1f6f7;
  }
  * { margin: 0; padding: 0; box-sizing: border-box; }
  html, body {
    width: 702px;
    height: 1200px;
    overflow: hidden;
    background: var(--card-teal);
  }
  .card {
    position: relative;
    width: 702px;
    height: 1200px;
    background: var(--card-teal);
    color: var(--ink-light);
    font-family: "Open Sans", "Segoe UI", sans-serif;
    text-align: center;
  }
  .line {
    position: absolute;
    left: 0;
    width: 100%;
    white-space: nowrap;
  }
  .holder-name {
    top: 296px;
    font-size: 45px;
    line-height: 48px;
    font-weight: 600;
  }
  .holder-role {
    top: 363px;
    font-size: 27px;
    line-height: 32px;
    font-weight: 400;
  }
  .services {
    font-size: 26px;
    line-height: 32px;
    font-weight: 400;
    letter-spacing: -0.2px;
  }
  .services.first { top: 465px; }
  .services.second { top: 516px; }
  .hours {
    top: 617px;
    font-size: 26px;
    line-height: 32px;
    font-weight: 400;
  }
  .contact {
    font-size: 31px;
    line-height: 36px;
    font-weight: 600;
  }
  .contact.phone { top: 715px; }
  .contact.mobile { top: 766px; }
  .contact.email { top: 816px; }
</style>
</head>
<body>
  <main class="card">
    <h1 class="line holder-name">Vandrell Osko</h1>
    <p class="line holder-role">Audiologue</p>

    <p class="line services first">Solutions Auditives | Protections Auditives</p>
    <p class="line services second">Acouphène | Hyperacousie</p>

    <p class="line hours">Sur RDV le Jeudi 14:00-18:00</p>

    <p class="line contact phone">Tel : 02/538 71 46</p>
    <p class="line contact mobile">GSM : 0482/37 58 90</p>
    <p class="line contact email">Email : v.osko@audiolinea.be</p>
  </main>
</body>
</html>
```